HTML Web Design for TelvoraLink Website

I require a non functioning web design in HTML format.
The website is for an online platform for connecting contract geoscientists with employers looking for short term geologists and geophysicists.
There will be 12 pages plus 3 sub pages of design to complete in total, but for your submission, please provide three pages and one sub page for review. These are to be submitted upon you winning the design contest, and then you can complete the rest of the pages in the days following that.
Please provide your designs for the Home Page, Contractor Profile Page and the Search Page / Search Results List.
Please review my design brief, and mockup of some of the pages carefully. Also, please find attached my logo.
Note, my logo is red, but I do not want a red dominated design, please use red as an accent colour.

Target Market(s)

Geoscientists

Industry/Entity Type

Oil And Gas

Number of Pages Required

5+ page

Requirements
Must have
• HTML format designs
• Submit 3 pages for competition, but further pages after winner is selected
• Professional and modern
Nice to have
• Some red accent
Should not have
• Too much red

```html
<!DOCTYPE html>
<html lang="en">
<head>
<meta charset="utf-8">
<title>TelvoraLink – Articles</title>
<link href="https://fonts.googleapis.com/css2?family=Raleway:wght@400;500;600;700&display=swap" rel="stylesheet">
<style>
:root{
  --red:#e0223f;
  --ink:#222326;
  --text:#444;
  --muted:#6a6a6a;
  --line:#d8d8d8;
  --dark:#16171b;
  --panel:#ececec;
  --foot:#f5f5f5;
  --copy:#d6d6d6;
  --badge:#2a8fd4;
}
*{box-sizing:border-box;margin:0;padding:0}
html,body{width:860px;height:1200px;overflow:hidden}
body{position:relative;background:#fff;font-family:"Raleway",sans-serif;color:var(--text)}

/* header */
.hero-shape{position:absolute;left:0;top:0}
.brand{position:absolute;left:14px;top:30px;font-size:22px;font-weight:700;color:var(--red);display:flex;align-items:center;gap:6px}
.brand .mark{width:14px;height:14px;background:var(--red)}
.util-nav{position:absolute;left:496px;top:0;width:320px;height:32px;display:flex;align-items:center;justify-content:center;gap:10px;font-size:11px;color:#fff}
.util-nav b{color:var(--ink);font-weight:700}
.util-nav .sep{opacity:.8}
.main-nav{position:absolute;top:51px;right:112px;display:flex;gap:15px;font-size:10.2px;font-weight:500;color:var(--ink);white-space:nowrap}
.search-btn{position:absolute;left:760px;top:46px;width:24px;height:24px;border:2px solid var(--red);border-radius:50%}
.page-title{position:absolute;left:100px;top:132px;display:flex;align-items:center;gap:12px;color:#fff;font-size:20px;font-weight:600}

/* cards */
.card{position:absolute;width:211px;background:#fff;border:1px solid var(--line)}
.card .photo{height:157px}
.card .body{padding:9px 16px 0 15px}
.card h3{font-size:13px;font-weight:600;color:var(--ink);margin-bottom:8px;white-space:nowrap}
.card p{font-size:7.8px;line-height:14.7px;text-align:justify;color:var(--text)}
.card .actions{display:flex;align-items:center;margin-top:10px}
.btn{display:inline-block;border:1.5px solid var(--red);color:var(--red);font-size:9px;font-weight:700;width:68px;height:22px;line-height:19px;text-align:center}
.source{display:flex;align-items:center;gap:7px;margin-left:21px;font-size:10.5px;font-weight:700;color:var(--ink)}
.source .dot{width:21px;height:21px;border-radius:50%;background:var(--badge)}

/* rss */
.rss{position:absolute;left:0;top:793px;width:860px;height:147px;background:var(--dark);color:#fff}
.rss h2{position:absolute;left:127px;top:18px;font-size:20px;font-weight:600}
.rss-icon{position:absolute;left:90px;top:22px}
.rss-item{position:absolute;top:56px;width:220px}
.rss-item h4{font-size:11.5px;font-weight:600;margin-bottom:9px;white-space:nowrap}
.rss-item p{font-size:8px;line-height:15px;color:#ddd}

/* contact */
.contact{position:absolute;left:0;top:940px;width:860px;height:208px;background:var(--panel)}
.contact h2{position:absolute;font-size:19px;font-weight:600;color:var(--ink)}
.field{position:absolute;border-bottom:1.5px solid var(--red);font-size:11px;color:var(--ink);padding-left:2px;height:20px}
.submit{position:absolute;left:88px;top:155px;width:80px;height:26px;border:1.5px solid var(--red);color:var(--red);font-size:11px;font-weight:700;text-align:center;line-height:23px}
.info{position:absolute;left:606px;font-size:8.8px;line-height:14.5px;color:var(--ink);display:flex;gap:8px}
.info svg{flex:none;margin-top:2px}
.social{position:absolute;left:606px;top:160px;display:flex;gap:5px}
.social span{width:20px;height:20px;border-radius:50%;background:#a8a8a8}

/* footer */
.foot-nav{position:absolute;left:0;top:1148px;width:860px;height:24px;background:var(--foot);display:flex;justify-content:center;align-items:center;gap:21px;font-size:8.8px;color:var(--ink)}
.copyright{position:absolute;left:0;top:1172px;width:860px;height:28px;background:var(--copy);font-size:7.8px;color:var(--ink);text-align:center;line-height:27px}
</style>
</head>
<body>

<svg class="hero-shape" width="860" height="460" viewBox="0 0 860 460">
  <defs>
    <linearGradient id="heroTone" x1="0" y1="0" x2="0" y2="1">
      <stop offset="0" stop-color="#3b3b3d"/>
      <stop offset="0.45" stop-color="#4a4038"/>
      <stop offset="0.75" stop-color="#9a5a2c"/>
      <stop offset="1" stop-color="#4a3326"/>
    </linearGradient>
  </defs>
  <polygon points="144,82 490,82 390,190 390,456 0,456 0,196" fill="url(#heroTone)" role="img" aria-label="Photo of an offshore oil platform and pipeline at sunset"/>
  <line x1="250" y1="0" x2="0" y2="196" stroke="var(--red)" stroke-width="2"/>
  <polygon points="496,0 816,0 790,32 522,32" fill="var(--red)"/>
</svg>

<div class="brand"><span class="mark"></span>TelvoraLink</div>

<nav class="util-nav">
  <span>Job Postings</span><span class="sep">|</span>
  <span>Resources</span><span class="sep">|</span>
  <b>Articles</b><span class="sep">|</span>
  <span>Contact</span>
</nav>
<nav class="main-nav">
  <span>Home</span><span>How it Works</span><span>Contractor Profile</span><span>Employer Favourites</span><span>Analytics</span>
</nav>
<div class="search-btn">
  <svg width="20" height="20" viewBox="0 0 20 20"><circle cx="9" cy="9" r="3.6" fill="none" stroke="var(--red)" stroke-width="1.8"/><line x1="11.6" y1="11.6" x2="14" y2="14" stroke="var(--red)" stroke-width="1.8"/></svg>
</div>

<div class="page-title">
  <svg width="20" height="20" viewBox="0 0 20 20"><rect x="2" y="4" width="13" height="13" rx="2" fill="none" stroke="#fff" stroke-width="1.6"/><path d="M8 12 L17 3 L19 5 L10 14 L7.5 14.5 Z" fill="#fff"/></svg>
  Articles
</div>

<!-- column 1 -->
<article class="card" style="left:102px;top:182px;height:461px">
  <div class="photo" role="img" aria-label="Photo of two hikers looking up at a rock cliff" style="background:linear-gradient(135deg,#5f7a45,#a78a6a 60%,#c9b49a)"></div>
  <div class="body">
    <h3>Finibus Bonorum et Malorum</h3>
    <p>Et harum quidem rerum facilis est et expedita distinctio. Nam libero tempore, cum soluta nobis est eligendi optio cumque nihil impedit quo minus id quod maxime placeat facere possimus, omnis voluptas assumenda est, omnis dolor repellendus. Temporibus autem quibusdam et aut officiis debitis aut rerum necessitatibus saepe eveniet ut et voluptates repudiandae sint et molestiae non recusandae. Itaque earum rerum hic tenetur a sapiente delectus, ut aut reiciendis voluptatibus maiores alias consequatur aut perferendis doloribus asperiores repellat. Itaque earum rerum hic tenetur a sapiente delectus, ut aut reiciendis voluptatibus maiores alias consequatur asperiores repellat.</p>
    <div class="actions" style="margin-top:9px"><span class="source" style="margin-left:89px"><span class="dot"></span>DRILLPOINT</span></div>
  </div>
</article>
<article class="card" style="left:102px;top:642px;height:134px">
  <div class="body" style="padding-top:15px">
    <h3>Finibus Bonorum et Malorum</h3>
    <p>Et harum quidem rerum facilis est et expedita distinctio. Nam libero tempore, cum soluta nobis est eligendi optio ...</p>
    <div class="actions"><span class="btn">Read more</span><span class="source"><span class="dot"></span>DRILLPOINT</span></div>
  </div>
</article>

<!-- column 2 -->
<article class="card" style="left:325px;top:182px;height:290px">
  <div class="photo" role="img" aria-label="Photo of an engineer in a hard hat reading a tablet on site" style="background:linear-gradient(135deg,#8fb3d6,#c4a45a 45%,#4d5f7a)"></div>
  <div class="body">
    <h3>Finibus Bonorum et Malorum</h3>
    <p>Et harum quidem rerum facilis est et expedita distinctio. Nam libero tempore, cum soluta nobis est eligendi optio ...</p>
    <div class="actions"><span class="btn">Read more</span><span class="source"><span class="dot"></span>DRILLPOINT</span></div>
  </div>
</article>
<article class="card" style="left:325px;top:486px;height:290px">
  <div class="photo" role="img" aria-label="Photo of two workers at a refinery with pipes and towers" style="background:linear-gradient(160deg,#6d88a8,#3c4a60 55%,#1f2633)"></div>
  <div class="body">
    <h3>Finibus Bonorum et Malorum</h3>
    <p>Et harum quidem rerum facilis est et expedita distinctio. Nam libero tempore, cum soluta nobis est eligendi optio ...</p>
    <div class="actions"><span class="btn">Read more</span><span class="source"><span class="dot"></span>DRILLPOINT</span></div>
  </div>
</article>

<!-- column 3 -->
<article class="card" style="left:548px;top:182px;height:290px">
  <div class="photo" role="img" aria-label="Photo of construction workers among steel rebar columns" style="background:linear-gradient(160deg,#8a8f95,#5a4a3e 55%,#3a342f)"></div>
  <div class="body">
    <h3>Finibus Bonorum et Malorum</h3>
    <p>Et harum quidem rerum facilis est et expedita distinctio. Nam libero tempore, cum soluta nobis est eligendi optio ...</p>
    <div class="actions"><span class="btn">Read more</span><span class="source"><span class="dot"></span>DRILLPOINT</span></div>
  </div>
</article>
<article class="card" style="left:548px;top:486px;height:290px">
  <div class="photo" role="img" aria-label="Photo of an offshore oil platform at sunset" style="background:linear-gradient(180deg,#6c6a68,#b07238 60%,#3a2a20)"></div>
  <div class="body">
    <h3>Finibus Bonorum et Malorum</h3>
    <p>Et harum quidem rerum facilis est et expedita distinctio. Nam libero tempore, cum soluta nobis est eligendi optio ...</p>
    <div class="actions"><span class="btn">Read more</span><span class="source"><span class="dot"></span>DRILLPOINT</span></div>
  </div>
</article>

<section class="rss">
  <svg class="rss-icon" width="18" height="18" viewBox="0 0 18 18"><circle cx="3" cy="15" r="2.4" fill="#fff"/><path d="M1 8 A9 9 0 0 1 10 17" fill="none" stroke="#fff" stroke-width="2.4"/><path d="M1 2 A15 15 0 0 1 16 17" fill="none" stroke="#fff" stroke-width="2.4"/></svg>
  <h2>RSS Feed</h2>
  <div class="rss-item" style="left:86px"><h4>Neque porro quisquam est qui dolorem</h4><p>Lorem Ipsum is simply dummy text of the printing and typesetting industry.</p></div>
  <div class="rss-item" style="left:326px"><h4>Neque porro quisquam est qui dolorem</h4><p>Lorem Ipsum is simply dummy text of the printing and typesetting industry.</p></div>
  <div class="rss-item" style="left:561px"><h4>Neque porro quisquam est qui dolorem</h4><p>Lorem Ipsum is simply dummy text of the printing and typesetting industry.</p></div>
</section>

<section class="contact">
  <h2 style="left:86px;top:20px">Contact Us</h2>
  <div class="field" style="left:88px;top:56px;width:217px">Name</div>
  <div class="field" style="left:322px;top:56px;width:218px">Email</div>
  <div class="field" style="left:88px;top:106px;width:452px;padding-left:4px">Message</div>
  <div class="submit">Submit</div>

  <h2 style="left:606px;top:20px">Location</h2>
  <div class="info" style="top:64px">
    <svg width="10" height="12" viewBox="0 0 10 12"><path d="M5 0 A4.5 4.5 0 0 1 9.5 4.5 C9.5 7.5 5 12 5 12 C5 12 0.5 7.5 0.5 4.5 A4.5 4.5 0 0 1 5 0 Z" fill="var(--ink)"/><circle cx="5" cy="4.5" r="1.7" fill="var(--panel)"/></svg>
    <span>Main Office 2210 Harlow<br>Ave South Houston</span>
  </div>
  <div class="info" style="top:108px">
    <svg width="10" height="10" viewBox="0 0 10 10"><path d="M2 0 L4 2.5 L3 4 Q4.5 6 6 7 L7.5 6 L10 8 L8.5 10 Q3 9 0 1.5 Z" fill="var(--ink)"/></svg>
    <span>(555)-014-2287</span>
  </div>
  <div class="info" style="top:130px">
    <svg width="10" height="8" viewBox="0 0 10 8"><rect width="10" height="8" fill="var(--ink)"/><path d="M0 0 L5 4.5 L10 0" fill="none" stroke="var(--panel)" stroke-width="1"/></svg>
    <span>info@telvoralink.com</span>
  </div>
  <div class="social"><span></span><span></span><span></span><span></span></div>
</section>

<nav class="foot-nav">
  <span>Home</span><span>Contractor Profile</span><span>Employer Search</span><span>Contract job Posting</span><span>Articles</span><span>Resources</span><span>Payment Checkout</span><span>Contact Us</span>
</nav>
<div class="copyright">Copyrights © 2017, www.telvoralink.com. All Rights Reserved.</div>

</body>
</html>
```